Podiatry (services) Business Card

I need a business design for a New Podiatry Service.
the Podiatry services will include all aspects of podiatry including;
general podiatry for all ages
corns and callus treatment
Ingrown toenails & nail surgery
Forefoot, arch and heel pain
Gait analysis
Sports Podiatry and Orthotics
Paediatric Assessments
Diabetes Foot Assessment

I would like the back of the card to have space for next appointment day and time.

I would like a nice design that is simple yet catchy. I don't like cluttered business cards. I like things to be simple yet stand out because of the finer details.

I like the colours blue and white but I'm open to other designs that have different colours.

Industry/Entity Type

Business

Contact Information for Business Card

Cobaltline Podiatry (Business name)

Delphine Marrow - Podiatrist
M.Pod.P., B.Hlth. Sci, MQFodE

Address: 17 Tolbrook Rd, Harwick Vale Qld, 4127
Phone: (03) 9462 3178
Fax: (03) 9514 2683

```html
<!DOCTYPE html>
<html lang="en">
<head>
<meta charset="utf-8">
<title>Cobaltline Podiatry – Business Card</title>
<link href="https://fonts.googleapis.com/css2?family=Open+Sans:wght@400;500;600&display=swap" rel="stylesheet">
<style>
  :root {
    --backdrop: #3b3440;
    --card-white: #ffffff;
    --brand-blue: #1f6fc4;
    --band-blue-start: #1d5cb4;
    --band-blue-end: #2f86cf;
    --back-blue-start: #1e5cb6;
    --back-blue-end: #3588cd;
    --ink-light: #ffffff;
    --card-shadow: rgba(0, 0, 0, 0.35);
  }
  * { margin: 0; padding: 0; box-sizing: border-box; }
  html, body {
    width: 1200px;
    height: 1000px;
    overflow: hidden;
    background: var(--backdrop);
    font-family: "Open Sans", Arial, sans-serif;
  }
  .canvas {
    position: relative;
    width: 1200px;
    height: 1000px;
    display: flex;
    flex-direction: column;
    align-items: center;
    justify-content: center;
    gap: 70px;
  }
  .card {
    position: relative;
    width: 630px;
    height: 360px;
    border-radius: 4px;
    overflow: hidden;
    box-shadow: 0 14px 34px var(--card-shadow);
  }

  /* Front */
  .card-front { background: var(--card-white); }
  .brand-name {
    position: absolute;
    top: 62px;
    left: 0;
    right: 0;
    text-align: center;
    font-size: 30px;
    font-weight: 500;
    letter-spacing: 0.5px;
    color: var(--brand-blue);
  }
  .name-band {
    position: absolute;
    top: 128px;
    left: 0;
    right: 0;
    height: 122px;
    background: linear-gradient(90deg, var(--band-blue-start), var(--band-blue-end));
    color: var(--ink-light);
    padding: 22px 0 0 88px;
  }
  .practitioner-name {
    font-size: 31px;
    font-weight: 500;
    line-height: 1.2;
  }
  .credentials {
    font-size: 19px;
    font-weight: 400;
    margin-top: 4px;
    letter-spacing: 0.3px;
  }

  /* Back */
  .card-back {
    background: linear-gradient(200deg, var(--back-blue-end), var(--back-blue-start));
    color: var(--ink-light);
  }
  .contact-block {
    position: absolute;
    left: 34px;
    bottom: 34px;
    font-size: 17px;
    line-height: 1.55;
  }
  .pin-row {
    height: 20px;
    margin-bottom: 6px;
    padding-left: 228px;
  }
  .contact-line { display: flex; align-items: center; gap: 8px; white-space: nowrap; }
  .contact-item { display: inline-flex; align-items: center; gap: 7px; }
  .contact-item + .contact-item { margin-left: 26px; }
  .icon { width: 15px; height: 15px; fill: var(--ink-light); flex: none; }
</style>
</head>
<body>
<main class="canvas">

  <section class="card card-front" aria-label="Business card front">
    <div class="brand-name">COBALTLINE PODIATRY</div>
    <div class="name-band">
      <div class="practitioner-name">Delphine Marrow - Podiatrist</div>
      <div class="credentials">M.Pod.P., B.Hlth. Sci, MQFodE</div>
    </div>
  </section>

  <section class="card card-back" aria-label="Business card back">
    <div class="contact-block">
      <div class="pin-row">
        <svg class="icon" viewBox="0 0 24 24" aria-hidden="true">
          <path d="M12 2a7 7 0 0 0-7 7c0 5.2 7 13 7 13s7-7.8 7-13a7 7 0 0 0-7-7zm0 9.6A2.6 2.6 0 1 1 12 6.4a2.6 2.6 0 0 1 0 5.2z" fill="none" stroke="#ffffff" stroke-width="2"/>
        </svg>
      </div>
      <div class="contact-line">Address: 17 Tolbrook Rd, Harwick Vale Qld, 4127</div>
      <div class="contact-line">
        <span class="contact-item">
          <svg class="icon" viewBox="0 0 24 24" aria-hidden="true">
            <path d="M6.6 10.8a15.1 15.1 0 0 0 6.6 6.6l2.2-2.2c.3-.3.7-.4 1-.2 1.1.4 2.3.6 3.6.6.6 0 1 .4 1 1V20c0 .6-.4 1-1 1A17 17 0 0 1 3 4c0-.6.4-1 1-1h3.5c.6 0 1 .4 1 1 0 1.3.2 2.5.6 3.6.1.3 0 .7-.2 1z"/>
          </svg>
          Phone: (03) 9462 3178
        </span>
        <span class="contact-item">
          <svg class="icon" viewBox="0 0 24 24" aria-hidden="true">
            <path d="M7 2h8l2 2v5H7zM4 9h16a2 2 0 0 1 2 2v7h-4v4H6v-4H2v-7a2 2 0 0 1 2-2zm4 8v3h8v-3z"/>
          </svg>
          Fax: (03) 9514 2683
        </span>
      </div>
    </div>
  </section>

</main>
</body>
</html>
```